Media and Film Company Needs a New Website

We produce highly stylized commercials and film pieces for our clients. We also produce live events, both corporate and theatrical. Looking for a site that can show off our client videos - have a polished way to show off our team, and be able to create pages to highlight our clients and give a full overview of our project/process with them. We design simple website for some of our clients - so we are very wordpress familiar, and would like something that doesn't feel like a template.

Target Market(s)

content creators, creative directors, production teams, marketing agencies

Industry/Entity Type

Film Production

Number of Pages Required

4 page

Font styles to use
Sans Serif

Requirements
Must have
• slick looking video embed (from YT or Vimeo)
• project pages - client snapshot (what we did for them, how we did it)
• nice landing page, have our company video reel on the page
• testimonials
• contact page
• ability to have photos as a background if we want
Nice to have
• polished clean look - look to our logo colors and linear elements
• we produce very stylized videos for our clients and our website should reflect that
Should not have
• template look or feel to it- please bring your flare to the project!
• take a look at our current site - zantorvo.com we need a better way to highlight our work and our clients

```html
<!DOCTYPE html>
<html lang="en">
<head>
<meta charset="utf-8">
<title>Zantorvo Media &amp; Entertainment</title>
<link rel="stylesheet" href="https://fonts.googleapis.com/css2?family=Montserrat:wght@400;500;600;700&family=PT+Sans:wght@400;700&family=Open+Sans:wght@300;400;600&display=swap">
<style>
:root{
  --wood-dark:#2a1c17;
  --wood:#3b2923;
  --band:#2e1f1a;
  --ink:#1c1c1c;
  --text:#555;
  --white:#fff;
  --gold:#f3be1b;
  --magenta:#e0245a;
  --blue:#1ea7e1;
  --grey-band:#e8e8e8;
  --footer:#131313;
  --footer-text:#bfbfbf;
  --bottom-bar:#2a1d17;
}
*{margin:0;padding:0;box-sizing:border-box}
html,body{width:1200px;height:2287px;overflow:hidden}
body{position:relative;background:var(--white);font-family:"PT Sans",Arial,sans-serif;color:var(--text)}
.abs{position:absolute}

/* hero */
.hero{left:0;top:0;width:1200px;height:570px;
  background:repeating-linear-gradient(90deg,#3a2822 0 38px,#33231e 38px 40px,#402c25 40px 86px,#2f201b 86px 88px);}
.hero-shade{left:0;top:0;width:1200px;height:570px;background:linear-gradient(180deg,rgba(0,0,0,.35),rgba(0,0,0,0) 30%,rgba(0,0,0,0) 70%,rgba(0,0,0,.25))}
.brand{left:76px;top:58px;font-family:"Montserrat",sans-serif;font-weight:700;font-size:20px;letter-spacing:.5px;color:var(--white);display:flex;align-items:center;gap:8px;white-space:nowrap}
.brand-mark{width:10px;height:10px;background:var(--gold)}
.nav{left:331px;top:43px;width:805px;height:61px;border:2px solid #6a5a52;border-radius:31px;background:rgba(20,12,10,.55);
  display:flex;align-items:center;padding:0 2px;font-family:"Montserrat",sans-serif;font-size:16px;color:var(--white)}
.nav a{color:inherit;text-decoration:none;text-align:center;white-space:nowrap}
.nav .active{width:113px;height:53px;line-height:53px;border-radius:27px;background:var(--gold);color:var(--magenta)}
.nav .item{flex:1}
.slide-left{left:0;top:172px;width:262px;height:313px;background:linear-gradient(180deg,#2c3640 0%,#3d4a55 45%,#b5652e 72%,#3a2a22 100%)}
.slide-right{left:938px;top:172px;width:262px;height:313px;background:linear-gradient(120deg,#6c6a66,#3c3836 60%,#262220)}
.arrow{width:42px;height:52px;border-radius:26px;background:var(--gold);display:flex;align-items:center;justify-content:center}
.lights{left:0;top:485px;width:1200px;height:85px;
  background:
  radial-gradient(ellipse 40px 60px at 60px 100%,rgba(200,140,255,.45),transparent),
  radial-gradient(ellipse 40px 60px at 180px 100%,rgba(200,140,255,.45),transparent),
  radial-gradient(ellipse 40px 60px at 300px 100%,rgba(200,140,255,.45),transparent),
  radial-gradient(ellipse 40px 60px at 420px 100%,rgba(200,140,255,.45),transparent),
  radial-gradient(ellipse 40px 60px at 540px 100%,rgba(200,140,255,.45),transparent),
  radial-gradient(ellipse 40px 60px at 660px 100%,rgba(200,140,255,.45),transparent),
  radial-gradient(ellipse 40px 60px at 780px 100%,rgba(200,140,255,.45),transparent),
  radial-gradient(ellipse 40px 60px at 900px 100%,rgba(200,140,255,.45),transparent),
  radial-gradient(ellipse 40px 60px at 1020px 100%,rgba(200,140,255,.45),transparent),
  radial-gradient(ellipse 40px 60px at 1140px 100%,rgba(200,140,255,.45),transparent)}
.reel{left:262px;top:140px;width:676px;height:372px;border:4px solid #f2f2f2;background:#1d1d1d;box-shadow:0 6px 18px rgba(0,0,0,.6)}
.reel-title{left:0;top:106px;width:100%;text-align:center;font-family:"Montserrat",sans-serif;font-weight:700;font-size:32px;color:var(--white);letter-spacing:.5px;white-space:nowrap}
.reel-sub{left:0;top:218px;width:100%;text-align:center;font-family:"Open Sans",sans-serif;font-weight:300;font-size:72px;color:#e9e9e9;white-space:nowrap}
.controls{left:14px;bottom:8px;width:640px;height:22px;display:flex;align-items:center;gap:12px;color:#fff;font-family:"Open Sans",sans-serif;font-size:10px;font-weight:600}
.track{flex:1;height:6px;background:#2b2b2b;border:1px solid #444;position:relative}
.track i{position:absolute;left:0;top:-16px;background:#111;border:1px solid #777;padding:0 3px;font-style:normal;font-size:9px}

/* tagline band */
.tagband{left:0;top:570px;width:1200px;height:124px;background:var(--band)}
.tagline{left:81px;top:596px;font-family:"Open Sans",sans-serif;font-size:32px;color:var(--white);white-space:nowrap}
.motto{left:88px;top:636px;width:655px;display:flex;align-items:center;gap:18px;font-family:"Montserrat",sans-serif;font-size:19px;letter-spacing:11px;color:#5a4c46;white-space:nowrap}
.motto span.rule{flex:1;height:1px;background:#5a4c46}
.cta{left:915px;top:615px;width:209px;height:43px;border-radius:22px;background:var(--white);color:#333;font-family:"Open Sans",sans-serif;font-size:19px;text-align:center;line-height:43px}
.divider{left:0;width:1200px;height:2px;background:#111}

/* work thumbs */
.thumb{top:717px;height:236px;display:flex;align-items:center;justify-content:center}
.play{width:72px;height:72px;border-radius:50%;background:var(--white);display:flex;align-items:center;justify-content:center}

/* about */
.about-img{left:78px;top:1005px;width:521px;height:364px;background:linear-gradient(135deg,#2b2a2c,#6b5a54 45%,#b49a8a 60%,#3a3234);box-shadow:14px 14px 20px rgba(0,0,0,.3)}
.about-title{left:653px;top:1024px;font-family:"Montserrat",sans-serif;font-weight:600;font-size:36px;color:#111}
.about-copy{left:653px;top:1090px;width:470px;font-size:13.5px;line-height:21px;color:#555}
.about-copy p{margin-bottom:21px}

/* services */
.services{left:0;top:1418px;width:1200px;height:156px;background:var(--grey-band)}
.service-row{left:78px;top:1418px;width:1044px;height:156px;display:flex;box-shadow:0 10px 14px rgba(0,0,0,.12)}
.service{flex:1;display:flex;flex-direction:column;align-items:center;justify-content:flex-end;padding-bottom:22px;gap:14px;border-right:1px solid #f6f6f6;font-family:"Montserrat",sans-serif;font-size:17px;font-weight:500;color:var(--blue);white-space:nowrap}
.service.current{background:#f4f4f4;color:#111;border:1px solid #d9d9d9}
.service:last-child{border-right:0}

/* testimonial */
.testi-title{left:0;top:1634px;width:1200px;text-align:center;font-family:"Montserrat",sans-serif;font-weight:600;font-size:36px;color:#111}
.quote{left:160px;top:1700px;width:880px;text-align:center;font-family:"Open Sans",sans-serif;font-size:14.5px;line-height:22.5px;color:#666}
.qline{left:378px;top:1808px;width:450px;height:1px;background:#ccc}
.qbubble{left:330px;top:1788px}
.author{left:0;top:1822px;width:1200px;text-align:center;font-family:"Montserrat",sans-serif;font-size:20px;font-weight:500;color:#333}
.tnav{top:1730px}

/* footer */
.footer{left:0;top:1903px;width:1200px;height:331px;background:radial-gradient(ellipse at 60% 30%,#2a2a2a,var(--footer) 70%)}
.fcol{top:1955px;color:var(--footer-text);font-size:15px}
.fcol h4{font-family:"Open Sans",sans-serif;font-weight:400;font-size:20px;color:var(--white);margin-bottom:20px;letter-spacing:.3px}
.links li{list-style:none;line-height:31px;display:flex;align-items:center;gap:8px}
.feed{display:flex;gap:14px;margin-bottom:26px}
.avatar{width:52px;height:52px;border-radius:50%;background:linear-gradient(135deg,#c9c2ba,#6e6862);border:2px solid #ddd;flex:none}
.feed p{font-size:14px;line-height:20px;width:190px}
.feed small{display:block;font-size:13px;color:#8d8d8d}
.tweet{display:flex;gap:12px;margin-bottom:34px}
.tweet .dot{width:26px;height:26px;border-radius:50%;background:#6d6d6d;flex:none;margin-top:4px}
.tweet p{font-size:14px;line-height:20px}
.tweet small{display:block;font-size:13px;color:#8d8d8d}
.contact li{list-style:none;display:flex;gap:12px;margin-bottom:22px;line-height:23px;font-size:14px}
.goldline{left:0;top:2234px;width:1200px;height:4px;background:var(--gold)}
.bottombar{left:0;top:2238px;width:1200px;height:49px;background:var(--bottom-bar)}
.copy{left:80px;top:2251px;font-family:"Open Sans",sans-serif;font-size:14px;color:var(--white)}
.copy .yr{color:var(--magenta)}
.copy b{color:var(--gold);font-family:"Montserrat",sans-serif;font-weight:700}
.social{left:942px;top:2254px;display:flex;gap:24px}
.social span{width:14px;height:14px;border-radius:50%;background:#d8d8d8}
</style>
</head>
<body>

<!-- hero -->
<div class="abs hero"></div>
<div class="abs hero-shade"></div>
<div class="abs slide-left" role="img" aria-label="Video camera on a tripod against a dusk sky"></div>
<div class="abs slide-right" role="img" aria-label="Photographer holding a camera to his eye"></div>
<div class="abs lights"></div>

<div class="abs brand"><span>ZANTORVO MEDIA</span><span class="brand-mark"></span></div>

<nav class="abs nav">
  <a class="active" href="#">Home</a>
  <a class="item" href="#">Portfolio</a>
  <a class="item" href="#">About Zantorvo</a>
  <a class="item" href="#">Testimonial</a>
  <a class="item" href="#">Press</a>
  <a class="item" href="#">Contact Us</a>
</nav>

<div class="abs arrow" style="left:224px;top:302px">
  <svg width="12" height="14" viewBox="0 0 12 14"><path d="M8 2 3 7l5 5" fill="none" stroke="#222" stroke-width="2.5"/></svg>
</div>
<div class="abs arrow" style="left:934px;top:302px">
  <svg width="12" height="14" viewBox="0 0 12 14"><path d="M4 2l5 5-5 5" fill="none" stroke="#222" stroke-width="2.5"/></svg>
</div>

<div class="abs reel">
  <div class="abs reel-title">Zantorvo Media &amp; Entertainment</div>
  <div class="abs reel-sub">2015 Demo Reel</div>
  <div class="abs controls">
    <svg width="14" height="16" viewBox="0 0 14 16"><path d="M1 1l12 7-12 7z" fill="#fff"/></svg>
    <div class="track"><i>01:46</i></div>
    <svg width="18" height="10" viewBox="0 0 18 10"><g fill="#f08a1c"><rect x="0" y="7" width="3" height="3"/><rect x="4" y="5" width="3" height="5"/><rect x="8" y="3" width="3" height="7"/><rect x="12" y="0" width="3" height="10"/></g></svg>
    <span>HD</span>
    <svg width="10" height="10" viewBox="0 0 10 10"><path d="M0 0h3M0 0v3M10 0H7M10 0v3M0 10h3M0 10V7M10 10H7M10 10V7" stroke="#fff" stroke-width="2"/></svg>
  </div>
</div>

<!-- tagline -->
<div class="abs tagband"></div>
<div class="abs tagline">Professional video Creation &amp; Film Production</div>
<div class="abs motto"><span class="rule"></span>THE BEST OF THE BEST<span class="rule"></span></div>
<a class="abs cta">Contact Us Now</a>
<div class="abs divider" style="top:697px"></div>
<div class="abs divider" style="top:703px"></div>

<!-- work -->
<div class="abs thumb" style="left:78px;width:344px;background:linear-gradient(160deg,#1f4fa8,#4a6fb8 40%,#9ea6b0 70%,#2a2f3a)" role="img" aria-label="Events at a performing arts center, building at dusk">
  <div class="play"><svg width="20" height="24" viewBox="0 0 20 24"><path d="M2 1l17 11L2 23z" fill="#111"/></svg></div>
</div>
<div class="abs thumb" style="left:427px;width:346px;background:linear-gradient(150deg,#0d1a2e,#1e3456 50%,#0a1220)" role="img" aria-label="Conductor leading an orchestra on stage">
  <div class="play"><svg width="20" height="24" viewBox="0 0 20 24"><path d="M2 1l17 11L2 23z" fill="#111"/></svg></div>
</div>
<div class="abs thumb" style="left:778px;width:344px;background:linear-gradient(160deg,#6c7a88,#3f4c56 50%,#24303a)" role="img" aria-label="Man holding a bag of chips in a commercial spot">
  <div class="play"><svg width="20" height="24" viewBox="0 0 20 24"><path d="M2 1l17 11L2 23z" fill="#111"/></svg></div>
</div>

<!-- about -->
<div class="abs about-img" role="img" aria-label="Camera operator filming actors on a set"></div>
<h2 class="abs about-title">ABOUT US</h2>
<div class="abs about-copy">
  <p>Zantorvo Media &amp; Entertainment provides full-service campaigns in film and media production, live entertainment &amp; theatrical production, marketing &amp; advertising, and event management in the DC metro area.</p>
  <p>Founded in 2009, Zantorvo Media &amp; Entertainment has built a reputation working for clients including the Northlight Film Society, Meridian Leaders Forum, Halvern Music, Riverbend Community Partners, and Brightwell Events.</p>
  <p>Zantorvo Media &amp; Entertainment works to build strong relationships with its clients through full-service campaigns in multiple industries. Through community outreach, Zantorvo develops its campaigns thoroughly to provide the most successful services to its clients.</p>
</div>

<!-- services -->
<div class="abs services"></div>
<div class="abs service-row">
  <div class="service current">
    <svg width="96" height="76" viewBox="0 0 96 76"><circle cx="38" cy="38" r="36" fill="#1ea7e1"/><g fill="#fff"><circle cx="38" cy="20" r="8"/><circle cx="38" cy="56" r="8"/><circle cx="20" cy="38" r="8"/><circle cx="56" cy="38" r="8"/><circle cx="38" cy="38" r="4"/></g><path d="M66 66c10 6 24 2 26-10s-6-20-2-30" fill="none" stroke="#1ea7e1" stroke-width="4"/></svg>
    <span>Film &amp; Media Production</span>
  </div>
  <div class="service">
    <svg width="90" height="76" viewBox="0 0 90 76"><g fill="#333"><circle cx="22" cy="20" r="16"/><circle cx="54" cy="18" r="18"/><rect x="6" y="38" width="58" height="34" rx="4"/><path d="M66 48l22-12v38L66 62z"/></g></svg>
    <span>Live Production</span>
  </div>
  <div class="service">
    <svg width="40" height="76" viewBox="0 0 40 76"><rect x="12" y="2" width="16" height="40" rx="8" fill="#333"/><path d="M4 30c0 22 32 22 32 0M20 52v16M8 72h24" fill="none" stroke="#333" stroke-width="4"/></svg>
    <span>PR, Marketing &amp; Advertising</span>
  </div>
  <div class="service">
    <svg width="64" height="76" viewBox="0 0 64 76"><rect x="2" y="8" width="60" height="66" rx="6" fill="#333"/><g fill="#fff"><rect x="14" y="26" width="16" height="16" rx="2"/><rect x="34" y="26" width="16" height="16" rx="2"/><rect x="14" y="46" width="16" height="16" rx="2"/><rect x="34" y="46" width="16" height="16" rx="2"/></g><g fill="#333"><rect x="10" y="0" width="4" height="12"/><rect x="22" y="0" width="4" height="12"/><rect x="38" y="0" width="4" height="12"/><rect x="50" y="0" width="4" height="12"/></g></svg>
    <span>Events</span>
  </div>
</div>

<!-- testimonial -->
<h2 class="abs testi-title">Testimonial</h2>
<svg class="abs tnav" style="left:78px" width="30" height="40" viewBox="0 0 30 40"><path d="M1 2v36" stroke="#ccc"/><path d="M22 13l-8 7 8 7" fill="none" stroke="#bbb" stroke-width="2"/></svg>
<svg class="abs tnav" style="left:1092px" width="30" height="40" viewBox="0 0 30 40"><path d="M29 2v36" stroke="#222"/><path d="M8 13l8 7-8 7" fill="none" stroke="#222" stroke-width="2"/></svg>
<p class="abs quote">“Thank you very much for all the hard work and creativity that you devoted to the RCP video, which was moving and uplifting and captured the essence of what we try to do so very well. It made a strong and very positive impact on the guests at the dinner, and elicited many very favorable comments. I am grateful to you for the very significant contribution that you made to the success of our 18th annual Loretta Vance Benefit, and for all your help to RCP.”</p>
<div class="abs qline"></div>
<svg class="abs qbubble" width="48" height="50" viewBox="0 0 48 50"><path d="M24 3a20 20 0 1 1-10 37l-6 8 2-11A20 20 0 0 1 24 3z" fill="#fff" stroke="#ccc" stroke-width="2"/><path d="M18 18v10M28 18v10" stroke="#bbb" stroke-width="4"/></svg>
<div class="abs author">– Elena Marsh</div>

<!-- footer -->
<div class="abs footer"></div>

<div class="abs fcol" style="left:78px">
  <h4>Links</h4>
  <ul class="links">
    <li><svg width="8" height="14" viewBox="0 0 8 14"><path d="M1 1l6 6-6 6" fill="none" stroke="#ccc" stroke-width="1.5"/></svg>Home</li>
    <li><svg width="8" height="14" viewBox="0 0 8 14"><path d="M1 1l6 6-6 6" fill="none" stroke="#ccc" stroke-width="1.5"/></svg>About Us</li>
    <li><svg width="8" height="14" viewBox="0 0 8 14"><path d="M1 1l6 6-6 6" fill="none" stroke="#ccc" stroke-width="1.5"/></svg>Portfolio</li>
    <li><svg width="8" height="14" viewBox="0 0 8 14"><path d="M1 1l6 6-6 6" fill="none" stroke="#ccc" stroke-width="1.5"/></svg>Services</li>
    <li><svg width="8" height="14" viewBox="0 0 8 14"><path d="M1 1l6 6-6 6" fill="none" stroke="#ccc" stroke-width="1.5"/></svg>Testimonial</li>
    <li><svg width="8" height="14" viewBox="0 0 8 14"><path d="M1 1l6 6-6 6" fill="none" stroke="#ccc" stroke-width="1.5"/></svg>Contact Us</li>
  </ul>
</div>

<div class="abs fcol" style="left:328px">
  <h4>NEWS FEED</h4>
  <div class="feed"><div class="avatar" role="img" aria-label="Profile photo"></div><p>Clara Benton posted a new blog.<small>Today 5:60 pm - 12.06.2014</small></p></div>
  <div class="feed"><div class="avatar" role="img" aria-label="Profile photo"></div><p>Owen Pratt posted message on Clara Benton .<small>Today 2:05 pm - 13.06.2014</small></p></div>
</div>

<div class="abs fcol" style="left:605px">
  <h4>RECENT TWEETS</h4>
  <div class="tweet"><span class="dot"></span><p>@reelnorth@OwenPratt<br>Thank You..<small>4 day ago.</small></p></div>
  <div class="tweet"><span class="dot"></span><p>@reelnorth@OwenPratt<br>Thank You..<small>4 day ago.</small></p></div>
</div>

<div class="abs fcol" style="left:886px">
  <h4>Contact Us</h4>
  <ul class="contact">
    <li><svg width="16" height="20" viewBox="0 0 16 20"><path d="M8 1a7 7 0 0 1 7 7c0 5-7 11-7 11S1 13 1 8a7 7 0 0 1 7-7z" fill="none" stroke="#ccc" stroke-width="1.5"/><circle cx="8" cy="8" r="2.5" fill="none" stroke="#ccc" stroke-width="1.5"/></svg><span>Zantorvo Media &amp; Entertainment<br>4871 Alder Lane #210<br>Fairhaven, MD 20911</span></li>
    <li><svg width="18" height="18" viewBox="0 0 18 18"><path d="M4 1l3 4-2 2c1 3 3 5 6 6l2-2 4 3-2 3C8 17 1 10 1 3z" fill="#ddd"/></svg><span>555 014 2871</span></li>
    <li><svg width="18" height="14" viewBox="0 0 18 14"><rect x="1" y="1" width="16" height="12" fill="none" stroke="#ccc" stroke-width="1.5"/><path d="M1 1l8 7 8-7" fill="none" stroke="#ccc" stroke-width="1.5"/></svg><span>hello@zantorvo.com</span></li>
  </ul>
</div>

<div class="abs goldline"></div>
<div class="abs bottombar"></div>
<p class="abs copy">Copyright <span class="yr">©</span> 2017 <b>Zantorvo Media &amp; Entertainment</b>. All rights reserved</p>
<div class="abs social"><span></span><span></span><span></span><span></span><span></span></div>

</body>
</html>
```